2-Page Flyer for the Information Session about the Tranquil Venture Course

This is a flyer to announce/advertise an evening Information Session about the Tranquil Venture Course. This Program aims at mindfully rethinking and redesigning work (and life) for people who feel stuck or not entirely satisfied with their work and/or life (please see draft flyer attached for more details). This Program is property of Brightfold Joy, a company that uses a combination of Mindfulness, Design, and Entrepreneurship to help people achieve greater happiness (in their work and lives).
Updates

Target Market(s)

People who feel stuck or not entirely satisfied with their work and/or life (please see draft flyer attached for more details)

Font styles to use
Serif
Sans Serif

Colors
ffffff
f37122
33a6d7
acd037

Requirements
Must have
• All of what I will say below is suggestive (I’m not a design expert), and I’m open to divert from it, if it makes sense and feels more interesting.
• I thought initially of a 2-page flyer (please see draft flyer attached). The first page could help people grasp the essence of the event quickly (in 1 or 2 minutes), and then, if they are interested/motivated, they would continue reading through page 2, which has more info about the Program in itself.
• Potential Structure
• Page 1
• . About the Information Session on the Tranquil Venture Course
• . Visible Date & Time, Contacts, Venue (and other relevant info)
• . About me (the facilitator)
• Page 2
• . About the Tranquil Venture Course
• I include a Powerpoint draft of the flyer with the content. The design is rudimentary and precarious from an aesthetics/organization point of view, and this is mainly where I need help (and maybe in other aspects too!).
• On the flyer, I would like to include:
• . A photo of myself (I attach 1 picture).
• . 1 or 2 beautiful-nature photos (cropped or full). One may have to do with looking at the sky, dreaming, and imagining a new work and life (2 photos with sky and clouds attached). The other has to do with walking the transformation journey (the photo with the person walking through the forest path).
• . brightfold joy logo or logos (there are two slightly different ones, that can be used for different purposes). For the first page, I would like the brightfold joy logo that has "brightfold joy" written on the bottom, with the saying "Stillness, Craft and Venture for Joy" beneath. This is the main logo. For the 2nd page, you can choose the logo that adapts better.
• - Where it says the "the way out is in" it would be great to have a similar font to the one I attach (see file "Font_the_way_out_is_in.png" and Ankecallig-fg.ttf
Nice to have
• In terms of colours, I would not divert much from the logo colours (and of course white and black). I would like the flyer to be quite white. Almost like fairy-tale white: the white horse, the white snow, the white of the stars, the white heaven. White could be the base colour. White means peace, tranquillity, calm contentment, a smile.
• And then use the other colours. The green of the mindfulness. The blue of the sky, the dreams. And the orange of the sun, the energy, the fire, the action. And maybe the black for text.
• Where it says the "the way out is in" it would be great to have a similar font to the one I attach (see file "Font_the_way_out_is_in".
• I would like this flyer to be a piece of art, in every possible way. Simple, beautiful, ease, light, peaceful, calm happy. Just like the Tranquil Venture Course and brightfold joy Company that I am creating intends to be. The mission of this Program and Company is to be a designer, a painter (a Picasso) of happier and more fulfilling human lives.
• I am very much looking forward to seeing your proposal(s).

```html
<!DOCTYPE html>
<html lang="en">
<head>
<meta charset="utf-8">
<title>Tranquil Venture Course – Information Session</title>
<link rel="stylesheet" href="https://fonts.googleapis.com/css2?family=Jost:wght@400;500&family=Roboto+Condensed:wght@700&display=swap">
<style>
  :root {
    --orange: #ec8130;
    --blue: #33a6d7;
    --green: #acd037;
    --ink: #111111;
    --white: #ffffff;
    --sky-top: #1f6fc4;
    --sky-mid: #6aa6dd;
    --cloud: #e6edf6;
    --forest: #556d62;
    --panel: rgba(92, 104, 122, 0.72);
  }
  html, body { margin: 0; padding: 0; overflow: hidden; }
  body { width: 848px; height: 1200px; background: var(--white); }
  .flyer {
    position: relative;
    width: 848px;
    height: 1200px;
    overflow: hidden;
    font-family: "Jost", "Futura", sans-serif;
    color: var(--ink);
  }
  .sky-backdrop {
    position: absolute; inset: 0;
    background:
      radial-gradient(ellipse 420px 140px at 200px 420px, rgba(255,255,255,0.9), rgba(255,255,255,0) 70%),
      radial-gradient(ellipse 520px 200px at 600px 560px, rgba(255,255,255,0.85), rgba(255,255,255,0) 70%),
      radial-gradient(ellipse 600px 160px at 420px 760px, rgba(255,255,255,0.9), rgba(255,255,255,0) 70%),
      linear-gradient(180deg, var(--sky-top) 0%, #3b86d2 22%, var(--sky-mid) 38%, var(--cloud) 52%, #eef2f8 66%, #c9d3df 78%, var(--forest) 100%);
  }
  .brand {
    position: absolute; left: 438px; top: 34px;
    display: flex; align-items: center; gap: 16px;
  }
  .brand-dot { width: 86px; height: 86px; border-radius: 50%; background: var(--orange); }
  .brand-name {
    font-size: 40px; line-height: 36px; font-weight: 400; color: var(--blue);
    width: 220px;
  }
  .course-title {
    position: absolute; left: 28px; top: 42px; margin: 0;
    font-weight: 500; font-size: 93px; line-height: 90px;
    letter-spacing: -1px; color: var(--orange);
  }
  .course-title span { display: block; }
  .tagline {
    position: absolute; left: 441px; top: 234px; margin: 0;
    font-family: "Roboto Condensed", "Arial Narrow", sans-serif;
    font-weight: 700; font-size: 25px; line-height: 26.5px; color: var(--ink);
  }
  .event-when {
    position: absolute; left: 32px; top: 396px; margin: 0;
    font-size: 38px; line-height: 40.5px; font-weight: 400;
  }
  .booking {
    position: absolute; left: 32px; top: 592px; margin: 0;
    font-size: 15.5px; line-height: 18.8px;
  }
  .session-info { position: absolute; left: 345px; top: 396px; width: 400px; }
  .session-info h2 {
    margin: 0 0 6px; font-size: 26px; line-height: 27px; font-weight: 400;
  }
  .session-info p { margin: 0; font-size: 17px; line-height: 20.5px; }
  .session-info .who { margin-top: 34px; }
  .session-info .who p { width: 400px; }
  .facilitator {
    position: absolute; left: 31px; top: 867px; width: 737px; height: 284px;
    display: flex; background: var(--panel);
  }
  .facilitator-photo {
    width: 203px; height: 284px; flex: none;
    background: linear-gradient(160deg, #f2f2f2 0%, #bdbdbd 55%, #e6e6e6 100%);
  }
  .facilitator-bio { padding: 5px 16px 0 15px; color: var(--white); }
  .facilitator-bio h3 {
    margin: 0 0 5px; font-size: 15.5px; line-height: 19px; font-weight: 400; width: 200px;
  }
  .facilitator-bio p { margin: 0; font-size: 12.6px; line-height: 16.2px; }
</style>
</head>
<body>
<main class="flyer">
  <div class="sky-backdrop" role="img" aria-label="Photograph of blue sky above a sea of white clouds, with forested hills below"></div>

  <div class="brand">
    <div class="brand-dot"></div>
    <div class="brand-name">brightfold joy</div>
  </div>

  <h1 class="course-title">
    <span>Tranquil</span>
    <span>Venture</span>
    <span>Course</span>
  </h1>

  <p class="tagline">Stillness<br>Craft<br>Venture for Joy</p>

  <p class="event-when">Thursday<br>5th September<br>2019<br>19:30 to 21:00</p>

  <p class="booking">
    Information &amp; Booking:<br>
    Please contact for<br>
    more information or<br>
    to book a place<br>
    Email: info@brightfoldjoy.com<br>
    Tel: +34 611 204 573<br>
    (Video Call and Messaging)<br>
    Venue: Tidewater Coworking,<br>
    C/ Almendro 42, Barcelona
  </p>

  <section class="session-info">
    <div class="about">
      <h2>Information Session:</h2>
      <p>The purpose of this Information<br>Session is to give you a real insight<br>into the Tranquil Venture Course<br>and how it can help you get the<br>most out of your work and life.</p>
    </div>
    <div class="who">
      <h2>How much and<br>who can come?</h2>
      <p>The Information Session is free. Whether you come on your own, or with friends or family, you’ll be warmly welcome. It will take place on Thursday the 5th September 2019, from 19:30 to 21:00, at Tidewater Coworking. Please get in touch for more info or to book a place.</p>
    </div>
  </section>

  <section class="facilitator">
    <div class="facilitator-photo" role="img" aria-label="Black and white portrait photograph of the facilitator"></div>
    <div class="facilitator-bio">
      <h3>Facilitator: Dr Nuno Ferreira, Visiting Research Fellow, University of Avonmere</h3>
      <p>Nuno joined the University of Avonmere (School of Management) as a Lecturer in Entrepreneurship in 2015. He completed his PhD in Entrepreneurship at Kelvingrove Business School in 2014. His work received the Hartwell Doctoral Dissertation Award from the Society of Management Studies. He began his business career as a production engineer (Voltrix), and continued in sales (Norvatek). After his MBA, he worked as a strategy consultant at Douro Business School. Originally from Portugal, Nuno enjoys designing and launching new ideas, international communities, mindfulness retreats, and musical improvisation. He nurtures a close connection to Lotus Grove Mindfulness Centre, where he has practiced and volunteered over 9 months. He has a broad experience of sharing the benefits of mindfulness with others.</p>
    </div>
  </section>
</main>
</body>
</html>
```